Medical Centre Website

We need a new design for a medical centre based in Perth, Western Australia called 'Tarvin Grove Medical Centre'.

The medical centre does general practitioner work including general checkups, ecg, heart checks, woman's health and more servicing children and adults. They also do home visits on occasions where the patient cannot attend the centre.

They would like an information/brochure website where visitors can read up on the practice, send email and view their location.

The client wish the design to be clean, fresh and light. The main colours are a light purple/blue and to a dark navy blue. The client would not want the logo to be altered in any way. This includes changing the words colours or the image.

The final design should represent a loving, family friendly practice where patients can come to receive the best treatments.

We just need the end product to be presented to un in a layed psd format. The fonts must be as per the W3C standards.

**IMPORTANT**
I have received heaps of chatlink invites in the past. To treat everyone fairly, I do not add people to my chatlink list as in the past people expected us to give them the prize. If you have questions, please ask them in pixel forum as it may benefit others who are also designing the site. If I need to, I will send a message to the user.
Updates

Hi Designers,

Most designs we have received have been overly cluttered. Are you able to simplify the designs.

Cheers, Dorian

Hi Designers,

Some of the designs are quite attractive but aremore cluttered than I would like. If you have a look at the following design, the design is very simple and straight to the point. A lot of designs have too much wording and the reader can be put off. We are looking something more like:

velmoxa.com.au

I would prefer to see designs and have opened up the contest for a further 7 days.

Designers,

We have received feedback from the client and Quite frankly he don’t really like any of them.They are too cluttered and Americanised. All drab blue colours.
 
If you have a look at template monster, these designs are better and cleaner. We do not want heaps of writing on the front page.

If you look at the eariler examples such as quorbeyclinic.com.au which I did myself, the client loves that simplicity of the site.

```html
<!DOCTYPE html>
<html lang="en">
<head>
<meta charset="utf-8">
<title>Tarvin Grove Medical Centre</title>
<link href="https://fonts.googleapis.com/css2?family=Source+Sans+3:ital,wght@0,300;0,400;0,600;0,700;1,300;1,400&display=swap" rel="stylesheet">
<style>
:root{
  --navy:#1f3a80;
  --blue:#1b77c0;
  --sky:#2a8ccd;
  --nav-top:#1f74c2;
  --nav-bottom:#0b4a92;
  --lavender:#8e9bd6;
  --lavender-soft:#a8b2e0;
  --text:#555b66;
  --muted:#7d8390;
  --band:#eef1f8;
  --footer:#eff0f4;
  --rule:#d6d9e2;
}
*{margin:0;padding:0;box-sizing:border-box}
html,body{width:1035px;height:1200px;overflow:hidden;background:#fff}
body{position:relative;font-family:"Source Sans 3",sans-serif;color:var(--text)}
.abs{position:absolute}

/* header */
.brand{left:89px;top:40px;display:flex;align-items:center;gap:10px}
.brand-mark{width:22px;height:22px;border-radius:50%;background:var(--lavender)}
.brand-name{font-size:27px;font-weight:600;color:var(--navy);line-height:1;letter-spacing:.3px}
.enquiry{right:99px;top:42px;text-align:right}
.enquiry-label{font-size:16px;color:var(--lavender);line-height:1}
.enquiry-phone{font-size:25px;color:var(--navy);line-height:1.1}

/* nav */
.main-nav{left:0;top:105px;width:1035px;height:48px;background:linear-gradient(var(--nav-top),var(--nav-bottom));display:flex;padding-left:92px}
.main-nav a{color:#fff;text-decoration:none;font-size:17px;font-weight:300;line-height:48px;padding:0 22px;border-right:1px solid rgba(0,0,0,.22);box-shadow:1px 0 0 rgba(255,255,255,.12)}
.main-nav a:first-child{padding-left:23px}
.main-nav a:last-child{border-right:none;box-shadow:none}

/* hero */
.hero{left:0;top:153px;width:1035px;height:322px;background:#fff}
.hero-photo{left:377px;top:153px;width:580px;height:322px;background:linear-gradient(90deg,#ffffff 0%,#eef1f5 20%,#e3e8ef 55%,#f2f4f7 85%,#ffffff 100%)}
.hero-kicker{left:88px;top:230px;font-size:29px;font-weight:300;color:var(--sky)}
.hero-title{left:88px;top:263px;font-size:38px;font-weight:600;color:var(--navy)}
.hero-text{left:88px;top:311px;width:360px;font-size:13px;font-weight:300;color:var(--lavender);line-height:21px}
.hero-dots{left:89px;top:366px;display:flex;gap:4px}
.hero-dots span{width:13px;height:13px;border-radius:50%;background:var(--lavender-soft)}
.hero-dots span:first-child{background:var(--navy)}

/* services */
.services{left:0;top:475px;width:1035px;height:155px;background:radial-gradient(ellipse at center,#ffffff 45%,var(--band) 100%);border-top:1px solid #e3e6ee}
.slide-arrow{top:528px}
.service-img{width:80px;height:88px;border:1px solid #dde0e7;border-radius:2px}
.service-title{font-size:20px;color:var(--blue);font-weight:400;line-height:1}
.service-sub{font-size:12.5px;color:var(--text);line-height:1}
.service-text{font-size:11px;font-weight:300;color:var(--muted);line-height:16px}
.service-more{font-size:11px;font-weight:700;color:var(--navy);text-decoration:none}
.service-divider{width:1px;height:100px;top:502px;background:var(--rule)}

/* content */
h2.section{font-weight:400;color:var(--navy);line-height:1}
.welcome-title{left:89px;top:674px;font-size:25px}
.welcome-copy{left:90px;top:710px;width:545px;font-size:11px;line-height:16.8px;color:var(--text)}
.welcome-copy p{margin-bottom:8px}
.col-divider{left:660px;top:670px;width:1px;height:373px;background:var(--rule)}
.facilities-title{left:89px;top:855px;font-size:23px}
.facility-list{left:89px;top:892px;list-style:none}
.facility-list li{display:flex;align-items:center;gap:7px;height:24px;font-size:12px;color:var(--blue)}
.testimonials-title{left:383px;top:855px;font-size:23px}
.quote-open{left:370px;top:888px}
.author-photo{left:397px;top:892px;width:66px;height:61px;background:linear-gradient(#f0f1f3,#d7c2ad);border:1px solid #dadde3}
.quote-top{left:477px;top:887px;width:160px;font-size:10px;font-style:italic;font-weight:300;line-height:16.7px;color:var(--text)}
.quote-rule{left:394px;top:959px;width:242px;height:1px;background:var(--rule)}
.quote-bottom{left:394px;top:960px;width:245px;font-size:10px;font-style:italic;font-weight:300;line-height:16.7px;color:var(--text)}
.quote-close{display:inline-block;vertical-align:middle;margin-left:6px}
.quote-author{left:394px;top:1018px;font-size:10.5px;font-weight:600;color:var(--text)}

/* sidebar */
.team-photo{left:688px;top:666px;width:238px;height:105px;background:linear-gradient(#f6f7f9,#dfe3ea 60%,#c9cfd9)}
.team-title{left:692px;top:781px;font-size:18px;font-weight:400;color:#1c2230;letter-spacing:.2px;line-height:1}
.team-text{left:692px;top:803px;width:240px;font-size:12px;font-weight:300;line-height:20px;color:var(--text)}
.brochure-btn{left:691px;top:855px;width:234px;height:42px;border-radius:3px;background:linear-gradient(#a7b3e6,#7e8cd0);border:1px solid #7584c6;display:flex;align-items:center;padding-left:16px;gap:12px;color:#fff;font-size:17px;font-weight:300;text-decoration:none}
.appointment{left:692px;top:910px;width:236px;height:137px;border-radius:3px;overflow:hidden;border:1px solid #c9cfe0}
.appointment-photo{width:100%;height:100px;background:linear-gradient(90deg,#b9d6d2,#e8d8c6 45%,#f3e4d0 70%,#c8d9c4)}
.appointment-band{height:37px;background:linear-gradient(#1b5fb0,#0a3f85);color:#fff;font-size:16.5px;line-height:37px;padding-left:17px}

/* footer */
.site-footer{left:0;top:1093px;width:1035px;height:107px;background:var(--footer)}
.footer-nav{left:89px;top:1120px;display:flex;font-size:13px;color:var(--navy)}
.footer-nav a{color:var(--navy);text-decoration:none;padding:0 7px;border-left:1px solid var(--navy);line-height:14px}
.footer-nav a:first-child{padding-left:0;border-left:none}
.copyright{left:89px;top:1151px;font-size:11px;font-weight:300;color:var(--muted)}
.social{left:826px;top:1122px;display:flex;gap:8px}
.social span{width:23px;height:23px;border-radius:2px;background:var(--lavender)}
</style>
</head>
<body>

<header>
  <div class="abs brand">
    <span class="brand-mark"></span>
    <span class="brand-name">Tarvin Grove Medical Centre</span>
  </div>
  <div class="abs enquiry">
    <div class="enquiry-label">Enquiry Call Us</div>
    <div class="enquiry-phone">555.204.7318</div>
  </div>
</header>

<nav class="abs main-nav">
  <a href="#">Home</a><a href="#">About Us</a><a href="#">Treatments</a><a href="#">Medical Services</a><a href="#">Our Doctors</a><a href="#">Testimonials</a><a href="#">Contact</a>
</nav>

<section>
  <div class="abs hero"></div>
  <div class="abs hero-photo" role="img" aria-label="Photo of four smiling doctors in white coats with stethoscopes"></div>
  <div class="abs hero-kicker">Duis tincidunt lectus quis dui</div>
  <h1 class="abs hero-title">Medical Health Checkups</h1>
  <p class="abs hero-text">Mauris vel lacus vitae felis vestibulum volutpat Etiam est nunc venenatis in tristique eu imperdiet ac nisl</p>
  <div class="abs hero-dots"><span></span><span></span><span></span><span></span></div>
</section>

<section>
  <div class="abs services"></div>
  <svg class="abs slide-arrow" style="left:88px" width="22" height="44" viewBox="0 0 22 44"><path d="M20 2 L3 22 L20 42" fill="none" stroke="#b9c1e4" stroke-width="2"/></svg>
  <svg class="abs slide-arrow" style="left:927px" width="22" height="44" viewBox="0 0 22 44"><path d="M2 2 L19 22 L2 42" fill="none" stroke="#b9c1e4" stroke-width="2"/></svg>

  <div class="abs service-img" style="left:128px;top:507px;background:linear-gradient(135deg,#c9d3dc,#e8dcc6 60%,#b78b3e)" role="img" aria-label="Photo of a doctor reviewing notes with a patient"></div>
  <div class="abs service-title" style="left:216px;top:506px">Medical Checkups</div>
  <div class="abs service-sub" style="left:217px;top:531px">Mauris vel lacus vitae felis</div>
  <div class="abs service-text" style="left:217px;top:548px">Nunc tempus felis vitae urna.<br>Vivamus porttitor purus nisi</div>
  <a class="abs service-more" style="left:217px;top:584px" href="#">LEARN MORE ▸</a>
  <div class="abs service-divider" style="left:382px"></div>

  <div class="abs service-img" style="left:409px;top:507px;background:linear-gradient(135deg,#eef0f3,#f6f6f7 50%,#f0d6d6)" role="img" aria-label="Photo of a heart trace with a stethoscope"></div>
  <div class="abs service-title" style="left:498px;top:506px">Heart Tests</div>
  <div class="abs service-sub" style="left:498px;top:531px">Mauris vel lacus vitae felis</div>
  <div class="abs service-text" style="left:498px;top:548px">Nunc tempus felis vitae urna.<br>Vivamus porttitor purus nisi</div>
  <a class="abs service-more" style="left:498px;top:584px" href="#">LEARN MORE ▸</a>
  <div class="abs service-divider" style="left:659px"></div>

  <div class="abs service-img" style="left:688px;top:507px;background:linear-gradient(135deg,#d8dee5,#eef0f2 50%,#e7b9c4)" role="img" aria-label="Photo of a doctor talking with a female patient"></div>
  <div class="abs service-title" style="left:775px;top:506px">Women Health</div>
  <div class="abs service-sub" style="left:777px;top:531px">Mauris vel lacus vitae felis</div>
  <div class="abs service-text" style="left:777px;top:548px">Nunc tempus felis vitae urna.<br>Vivamus porttitor purus nisi</div>
  <a class="abs service-more" style="left:777px;top:584px" href="#">LEARN MORE ▸</a>
</section>

<main>
  <h2 class="abs section welcome-title">Welcome to Tarvin Grove Mainpage..</h2>
  <div class="abs welcome-copy">
    <p>Mauris vel lacus vitae felis vestibulum volutpat. Etiam est nunc, venenatis in, tristique eu, imperdiet ac, nisl. Cum soc iis natoque penatibus et magnis dis parturient montes, nascetur ridiculus mus.</p>
    <p>Mauris vel lacus vitae felis vestibulum volutpat. Etiam est nunc, venenatis in, tristique eu, imperdiet ac, nisl. Cum sociis natoque penatibus et magnis dis parturient montes, nascetur ridiculus massa. In iaculis facilisis massa. Etiam eu urna. Sed porta. Suspendisse quam leo, molestie sed, luctus quis, feugiat in, pede. Fusce tellus. Sed metus augue, convallis et, vehicula ut, pulvinar eu, ante</p>
  </div>
  <div class="abs col-divider"></div>

  <h2 class="abs section facilities-title">Facilities &amp; Care Provided</h2>
  <ul class="abs facility-list">
    <li><svg width="13" height="11" viewBox="0 0 13 11"><path d="M1 6 L5 10 L12 1" fill="none" stroke="#b5bde3" stroke-width="2.4"/></svg>Etiam est nunc venenatis</li>
    <li><svg width="13" height="11" viewBox="0 0 13 11"><path d="M1 6 L5 10 L12 1" fill="none" stroke="#b5bde3" stroke-width="2.4"/></svg>Cum sociis natoque penatibus magnis</li>
    <li><svg width="13" height="11" viewBox="0 0 13 11"><path d="M1 6 L5 10 L12 1" fill="none" stroke="#b5bde3" stroke-width="2.4"/></svg>Dis parturient montes nascetur ridiculus mus.</li>
    <li><svg width="13" height="11" viewBox="0 0 13 11"><path d="M1 6 L5 10 L12 1" fill="none" stroke="#b5bde3" stroke-width="2.4"/></svg>In iaculis facilisis massa.</li>
    <li><svg width="13" height="11" viewBox="0 0 13 11"><path d="M1 6 L5 10 L12 1" fill="none" stroke="#b5bde3" stroke-width="2.4"/></svg>Etiam eu urna Sed porta</li>
    <li><svg width="13" height="11" viewBox="0 0 13 11"><path d="M1 6 L5 10 L12 1" fill="none" stroke="#b5bde3" stroke-width="2.4"/></svg>Suspendisse quam leo molestie sed</li>
  </ul>

  <h2 class="abs section testimonials-title">Testimonials</h2>
  <svg class="abs quote-open" width="20" height="14" viewBox="0 0 20 14"><path d="M1 14 V8 Q1 2 7 0 L8 2 Q4 4 4 7 H8 V14 Z M11 14 V8 Q11 2 17 0 L18 2 Q14 4 14 7 H18 V14 Z" fill="#4a4f5a"/></svg>
  <div class="abs author-photo" role="img" aria-label="Portrait photo of the testimonial author"></div>
  <p class="abs quote-top">Nunc tempus felis vitae urna. Vivamus porttitor, neque at volut-pat rutrum, purus nisi eleifend libero, a tempus libero lectus</p>
  <div class="abs quote-rule"></div>
  <p class="abs quote-bottom">Morbi eget arcu. Morbi porta, libero id ullamcorper non-ummy, nibh ligula pulvinar metus, eget consectetuer augue nisi quis lacus. Ut ac mi quis lacus.<svg class="quote-close" width="15" height="10" viewBox="0 0 20 14"><path d="M19 0 V6 Q19 12 13 14 L12 12 Q16 10 16 7 H12 V0 Z M9 0 V6 Q9 12 3 14 L2 12 Q6 10 6 7 H2 V0 Z" fill="#4a4f5a"/></svg></p>
  <div class="abs quote-author">By Author Name</div>

  <aside>
    <div class="abs team-photo" role="img" aria-label="Group photo of the centre's doctors and team"></div>
    <h3 class="abs team-title">OUR DOCTORS &amp; TEAM</h3>
    <p class="abs team-text">Euismod in, elit. Fusce ultricies, orci ac feugiat suscipit, leo massa sodales velit</p>
    <a class="abs brochure-btn" href="#">DOWNLOAD BROCHURE
      <svg width="26" height="26" viewBox="0 0 26 26"><circle cx="13" cy="13" r="11.5" fill="none" stroke="#fff" stroke-width="2"/><path d="M7 13 H18 M13 8 L18 13 L13 18" fill="none" stroke="#fff" stroke-width="2.4"/></svg>
    </a>
    <div class="abs appointment">
      <div class="appointment-photo" role="img" aria-label="Photo of a smiling receptionist greeting a patient"></div>
      <div class="appointment-band">Make an Appointment Now</div>
    </div>
  </aside>
</main>

<footer>
  <div class="abs site-footer"></div>
  <nav class="abs footer-nav">
    <a href="#">Home</a><a href="#">About Us</a><a href="#">Treatments</a><a href="#">Medical Services</a><a href="#">Our Doctors</a><a href="#">Testimonials</a><a href="#">Contact</a>
  </nav>
  <div class="abs copyright">© 2013 Company Name.&nbsp; All right reserved.&nbsp; Term of Use</div>
  <div class="abs social" aria-label="Social links">
    <span aria-label="Social link one"></span><span aria-label="Social link two"></span><span aria-label="Social link three"></span><span aria-label="News feed"></span>
  </div>
</footer>

</body>
</html>
```